Cradle Quill

This is a single-page full-screen tablet app that generates baby names based on a few user-selected options. The code is already written; I just need the visual design.
UI elements are:
1) Options, containing:
i) Gender selector
ii) Multi-select
inspiration sources (names based on country of origin)
iii) Scroll speed selector
2) Favourites panel containing list of current favourites (with UI to delete items)
3) Output panel; a live scrolling list of generated names - click to add as a favourite.
The app is a Panelix 8 Tessel application, written in XAML. It should stick to the Tessel conventions/spirit. Here are some docs/samples:
http://docs.brightvane.example/library/panes/apps/qx482015/
http://en.lorepedia.example/wiki/Tessel_(design_language)
Ideally, design will be presented in XAML format.
The attached design is the crap I've got meanwhile - it shows the basic elements. The list of generated names appears in the white-space on the right. The bar on the bottom is an advertisement.
More on the Tessel design principles that should be adhered to:
http://www.brightvane.example/design/toolbox/tutorials/pane-handset-7/tessel/
Ideal submission would be in XAML format. However, Adobe Illustrator files are decent as well; vector format is important.
Pixel-based images aren't ideal in this case, because Tessel applications need to be scalable to any resolution.
Target Market(s)
People expecting a baby; mostly women.
Industry/Entity Type
Baby
Look and feel

```html
<!DOCTYPE html>
<html lang="en">
<head>
<meta charset="utf-8">
<title>Cradle Quill</title>
<link rel="stylesheet" href="https://fonts.googleapis.com/css2?family=Bebas+Neue&family=Lato:wght@300;400&display=swap">
<style>
  :root {
    --bg-deep: #137a3c;
    --bg-light: #0a9a48;
    --gender: #d42a52;
    --boy: #17c0e3;
    --girl: #f56f9c;
    --speed: #d9b801;
    --track: #6da7ee;
    --inspiration: #05c9e7;
    --name-a: #e5531f;
    --name-b: #f2903a;
    --list-a: #3ba717;
    --list-b: #8fd822;
    --list-head: #35a012;
    --white: #ffffff;
  }
  * { box-sizing: border-box; margin: 0; padding: 0; }
  html, body { width: 1200px; height: 585px; overflow: hidden; }
  body {
    position: relative;
    background: linear-gradient(120deg, var(--bg-deep) 0%, var(--bg-light) 45%, var(--bg-deep) 70%, var(--bg-light) 100%);
    font-family: "Lato", sans-serif;
    color: var(--white);
  }
  .tile { position: absolute; }
  .tile-title {
    position: absolute; left: 11px; top: 8px;
    font-family: "Bebas Neue", sans-serif; font-size: 27px; letter-spacing: .5px; line-height: 1;
  }
  .gender { left: 47px; top: 62px; width: 161px; height: 146px; background: var(--gender); }
  .gender-dot { position: absolute; top: 57px; width: 44px; height: 44px; border-radius: 50%; }
  .gender-dot.boy { left: 28px; background: var(--boy); }
  .gender-dot.girl { left: 86px; background: var(--girl); }
  .gender-label { position: absolute; top: 112px; font-family: "Bebas Neue", sans-serif; font-size: 17px; }
  .gender-label.boy { left: 36px; color: var(--boy); }
  .gender-label.girl { left: 95px; color: var(--girl); }

  .speed { left: 234px; top: 63px; width: 194px; height: 142px; background: var(--speed); }
  .speed-label { position: absolute; font-weight: 300; font-size: 15px; }
  .speed-label.slower { left: 5px; top: 42px; }
  .speed-label.faster { right: 8px; top: 89px; }
  .speed-track {
    position: absolute; left: 5px; top: 65px; width: 184px; height: 12px; border-radius: 6px;
    background: var(--white); overflow: hidden;
  }
  .speed-fill { width: 55%; height: 100%; background: var(--track); border-radius: 6px 0 0 6px; }

  .inspiration { left: 47px; top: 240px; width: 381px; height: 272px; background: var(--inspiration); }
  .flag { position: absolute; width: 86px; height: 64px; border: 3px solid var(--white); }
  .flag svg { display: block; width: 100%; height: 100%; }
  .flag-caption { position: absolute; left: 41px; top: 130px; width: 104px; text-align: center; font-size: 11px; }

  .baby-name {
    left: 459px; top: 52px; width: 313px; height: 460px;
    background: linear-gradient(135deg, var(--name-a), var(--name-b));
  }
  .baby-name .current {
    position: absolute; left: 0; right: 0; top: 170px; text-align: center;
    font-family: "Bebas Neue", sans-serif; font-size: 62px; letter-spacing: 1px;
  }
  .share { position: absolute; left: 10px; bottom: 12px; display: flex; align-items: center; gap: 3px; font-size: 15px; font-weight: 300; }

  .names {
    left: 804px; top: 57px; width: 313px; height: 455px;
    background: linear-gradient(160deg, var(--list-a) 30%, var(--list-b));
  }
  .names-head { height: 49px; background: var(--list-head); border-bottom: 1px solid rgba(255,255,255,.7); }
  .name-list { list-style: none; position: absolute; left: 8px; top: 56px; width: 297px; }
  .name-list li {
    height: 40.7px; padding: 10px 0 0 14px; font-size: 16px; font-weight: 300;
    border-bottom: 1px solid rgba(255,255,255,.85);
  }
  .alpha-index {
    position: absolute; left: 285px; top: 62px; width: 12px; list-style: none;
    font-size: 9px; line-height: 12.8px; text-align: center;
  }
  .diagonal { position: absolute; inset: 0; pointer-events: none; }
</style>
</head>
<body>
  <section class="tile gender">
    <h2 class="tile-title">Select Gender</h2>
    <span class="gender-dot boy"></span>
    <span class="gender-dot girl"></span>
    <span class="gender-label boy">Boy</span>
    <span class="gender-label girl">Girl</span>
  </section>

  <section class="tile speed">
    <span class="speed-label slower">slower</span>
    <div class="speed-track"><div class="speed-fill"></div></div>
    <span class="speed-label faster">faster</span>
  </section>

  <section class="tile inspiration">
    <h2 class="tile-title" style="top:16px">Inspiration</h2>
    <div class="flag" style="left:41px;top:62px">
      <svg viewBox="0 0 3 3" preserveAspectRatio="none"><rect width="3" height="1" fill="#fff"/><rect y="1" width="3" height="1" fill="#0c2fa3"/><rect y="2" width="3" height="1" fill="#d21a1a"/></svg>
    </div>
    <div class="flag" style="left:144px;top:62px">
      <svg viewBox="0 0 13 13" preserveAspectRatio="none">
        <rect width="13" height="13" fill="#fff"/>
        <g fill="#c8202f"><rect y="0" width="13" height="1"/><rect y="2" width="13" height="1"/><rect y="4" width="13" height="1"/><rect y="6" width="13" height="1"/><rect y="8" width="13" height="1"/><rect y="10" width="13" height="1"/><rect y="12" width="13" height="1"/></g>
        <rect width="5.5" height="7" fill="#2b3a7a"/>
      </svg>
    </div>
    <div class="flag" style="left:249px;top:62px">
      <svg viewBox="0 0 30 20" preserveAspectRatio="none"><rect width="30" height="20" fill="#d4140f"/><polygon points="5,2 6.2,5.4 9.8,5.4 6.9,7.6 8,11 5,8.9 2,11 3.1,7.6 0.2,5.4 3.8,5.4" fill="#ffde00"/><circle cx="11" cy="2.5" r=".9" fill="#ffde00"/><circle cx="13" cy="4.8" r=".9" fill="#ffde00"/><circle cx="13" cy="7.8" r=".9" fill="#ffde00"/><circle cx="11" cy="10" r=".9" fill="#ffde00"/></svg>
    </div>
    <span class="flag-caption">US NAMES</span>
    <div class="flag" style="left:41px;top:156px">
      <svg viewBox="0 0 3 3" preserveAspectRatio="none"><rect width="1" height="3" fill="#16803f"/><rect x="1" width="1" height="3" fill="#fff"/><rect x="2" width="1" height="3" fill="#f0802a"/></svg>
    </div>
    <div class="flag" style="left:144px;top:156px">
      <svg viewBox="0 0 3 3" preserveAspectRatio="none"><rect width="1" height="3" fill="#12843e"/><rect x="1" width="1" height="3" fill="#fff"/><rect x="2" width="1" height="3" fill="#c8202a"/></svg>
    </div>
    <div class="flag" style="left:249px;top:156px">
      <svg viewBox="0 0 30 21" preserveAspectRatio="none"><rect width="30" height="7" fill="#f08c2c"/><rect y="7" width="30" height="7" fill="#fff"/><rect y="14" width="30" height="7" fill="#138a3c"/><circle cx="15" cy="10.5" r="2.8" fill="none" stroke="#1b2c86" stroke-width=".6"/><circle cx="15" cy="10.5" r=".6" fill="#1b2c86"/></svg>
    </div>
  </section>

  <section class="tile baby-name">
    <h2 class="tile-title">Baby Name</h2>
    <p class="current">Giulia</p>
    <div class="share">
      <svg width="22" height="22" viewBox="0 0 22 22" aria-hidden="true"><g fill="#fff"><circle cx="17" cy="4.5" r="3.5"/><circle cx="5" cy="11" r="3.5"/><circle cx="17" cy="17.5" r="3.5"/></g><path d="M17 4.5 5 11l12 6.5" stroke="#fff" stroke-width="2" fill="none"/></svg>
      share
    </div>
  </section>

  <section class="tile names">
    <div class="names-head"><h2 class="tile-title" style="top:11px">Names</h2></div>
    <ul class="name-list">
      <li>Ada</li><li>Anastasia</li><li>Anna</li><li>Annamaria</li>
      <li>Adriana</li><li>Amalia</li><li>Almata</li><li>Andromeda</li>
    </ul>
    <ul class="alpha-index">
      <li>A</li><li>B</li><li>C</li><li>D</li><li>E</li><li>F</li><li>G</li><li>H</li><li>I</li><li>J</li><li>K</li><li>L</li><li>M</li><li>N</li><li>O</li><li>P</li><li>Q</li><li>R</li><li>S</li><li>T</li><li>U</li><li>V</li><li>W</li><li>X</li><li>Y</li><li>Z</li><li>#</li>
    </ul>
  </section>

  <svg class="diagonal" width="1200" height="585" viewBox="0 0 1200 585" aria-hidden="true">
    <line x1="0" y1="585" x2="1200" y2="0" stroke="#fff" stroke-width="1"/>
  </svg>
</body>
</html>
```